Social Media Graphics - Harbor Climb REVISED

Create 6-7 individual social media graphics (square size) to encourage folks to join our online course called:

The Lantern Ledger Plan
How to Launch a Multi-Million Business From Scratch
Sign Up Today!

IMPORTANT: Make the largest and most prominent text on the graphic be: How to Launch a Multi-Million Business From Scratch

For the color scheme of the graphics, let's try a blue color palette; make sure the graphics appeal to both men and women

Make sure each graphic contains 1 of the 3 pics attached (crop pic as needed); and make sure one of the graphics is all TEXT only.

Target Market(s)

men and women looking to start a business

Industry/Entity Type

Entrepreneurship

Colors
0054AA
0677BA
7BADD7
CADEEF
E8F1F8

Requirements
Must have
• All the text and use the 3 pics provided; one graphic can be all text; Simple, modern design that's easy to read

```html
<!DOCTYPE html>
<html lang="en">
<head>
<meta charset="utf-8">
<title>The Lantern Ledger Plan — Social Graphics</title>
<link href="https://fonts.googleapis.com/css2?family=Anton&family=Bebas+Neue&family=Montserrat:wght@400;500;600;700;800;900&family=Oswald:wght@300;500;700&display=swap" rel="stylesheet">
<style>
  :root{
    --board:#69a3c7;
    --blue:#0054aa;
    --blue-mid:#0677ba;
    --blue-light:#7badd7;
    --navy-dark:#041640;
    --pink:#f0345a;
    --white:#ffffff;
    --shadow:rgba(10,40,70,.35);
  }
  *{margin:0;padding:0;box-sizing:border-box}
  html,body{width:1200px;height:1195px;overflow:hidden}
  body{background:var(--board);position:relative;font-family:'Montserrat',sans-serif;color:var(--white)}
  .card{position:absolute;width:471px;height:471px;overflow:hidden;box-shadow:0 18px 22px -6px var(--shadow)}
  .card--presenters{left:84px;top:72px;background:linear-gradient(135deg,#0b3f98 0%,#0054aa 55%,#0a3d8c 100%)}
  .card--stage{left:647px;top:72px;background:linear-gradient(180deg,#1a4ca8 0%,#0f47a5 55%,#1a5ec0 100%)}
  .card--text{left:84px;top:634px;background:linear-gradient(160deg,#083b8e 0%,#0054aa 45%,#2a82d6 100%)}
  .card--duo{left:647px;top:634px;background:linear-gradient(140deg,#0c2f7d 0%,#06205a 55%,#0d3c96 100%)}
  .abs{position:absolute;line-height:1;white-space:nowrap}
  .photo{position:absolute}
  .condensed{font-family:'Bebas Neue','Oswald',sans-serif;font-weight:400}
  .headline{font-family:'Anton','Bebas Neue',sans-serif;font-weight:400;text-shadow:2px 2px 0 rgba(0,0,0,.35)}
  .heavy{font-weight:800}
  .tag-white{background:var(--white);color:var(--blue);font-weight:500;padding:3px 10px}
  .tag-pink{background:var(--pink);color:var(--white);font-weight:600;padding:3px 14px}
  .cta{position:absolute;display:flex;align-items:center;justify-content:center;font-weight:700;border:2px solid var(--white);border-radius:30px;letter-spacing:.3px}
  .cta--navy{background:var(--navy-dark)}
  .cta--pink{background:var(--pink)}
  .chevrons{position:absolute}
</style>
</head>
<body>

<section class="card card--presenters">
  <div class="photo" role="img" aria-label="Photo of the two course hosts smiling, arms crossed" style="left:0;top:100px;width:290px;height:371px;background:linear-gradient(90deg,#c8324f 0%,#7a2a3a 45%,#1a1a24 100%)"></div>
  <svg class="chevrons" style="left:10px;top:36px" width="22" height="42" viewBox="0 0 22 42" fill="none" stroke="#fff" stroke-width="2.5"><path d="M2 12 11 3 20 12M2 22 11 13 20 22M2 32 11 23 20 32M2 41 11 32 20 41"/></svg>
  <div class="abs" style="left:146px;top:28px;font-size:62px;font-family:'Oswald',sans-serif;font-weight:300">THE</div>
  <div class="abs condensed" style="left:252px;top:25px;width:219px;height:70px;background:var(--white);border-radius:16px 0 0 16px;color:var(--blue);font-size:56px;display:flex;align-items:center;justify-content:center">LANTERN</div>
  <div class="abs condensed" style="right:14px;top:106px;font-size:42px">LEDGER PLAN</div>
  <div class="abs tag-white" style="left:231px;top:194px;font-size:26px;transform:rotate(-3deg)">HOW TO</div>
  <div class="abs tag-pink" style="left:258px;top:228px;width:195px;font-size:26px;text-align:center">LAUNCH A</div>
  <div class="abs headline" style="right:20px;top:258px;font-size:60px">MULTI-MILLION</div>
  <div class="abs heavy" style="right:18px;top:326px;font-size:40px">BUSINESS</div>
  <div class="abs" style="right:20px;top:373px;font-size:33px;font-weight:400">FROM</div>
  <div class="abs heavy" style="right:20px;top:407px;font-size:41px">SCRATCH</div>
  <div class="cta cta--navy" style="left:25px;top:406px;width:150px;height:34px;font-size:12.5px">SIGN UP TODAY!</div>
</section>

<section class="card card--stage">
  <div class="photo" role="img" aria-label="Photo of the two hosts on stage, one speaking into a microphone" style="left:0;top:0;width:471px;height:260px;background:linear-gradient(180deg,#b9a89a 0%,#6c6a78 45%,#1f4ea4 100%)"></div>
  <div class="abs condensed" style="left:0;width:471px;text-align:center;top:20px;font-size:44px;text-shadow:2px 2px 0 rgba(0,0,0,.45)">THE LANTERN LEDGER PLAN</div>
  <svg class="chevrons" style="left:16px;top:190px" width="20" height="40" viewBox="0 0 20 40" fill="none" stroke="#fff" stroke-width="2.5"><path d="M2 3 10 11 18 3M2 13 10 21 18 13M2 23 10 31 18 23M2 31 10 39 18 31"/></svg>
  <svg class="chevrons" style="left:443px;top:332px" width="20" height="40" viewBox="0 0 20 40" fill="none" stroke="#fff" stroke-width="2.5"><path d="M2 11 10 3 18 11M2 21 10 13 18 21M2 31 10 23 18 31M2 39 10 31 18 39"/></svg>
  <svg style="position:absolute;left:424px;top:422px" width="18" height="18" viewBox="0 0 18 18"><circle cx="9" cy="9" r="7" fill="none" stroke="#7badd7" stroke-width="1.5"/></svg>
  <div class="abs tag-white" style="left:121px;top:193px;width:143px;height:38px;border-radius:20px;font-size:26px;display:flex;align-items:center;justify-content:center">HOW TO</div>
  <div class="abs tag-pink" style="left:146px;top:227px;width:195px;height:31px;border-radius:16px;font-size:26px;display:flex;align-items:center;justify-content:center">LAUNCH A</div>
  <div class="abs headline" style="left:0;width:471px;text-align:center;top:258px;font-size:60px">MULTI-MILLION</div>
  <div class="abs heavy" style="left:0;width:471px;text-align:center;top:324px;font-size:36px">BUSINESS</div>
  <div class="abs heavy" style="left:80px;top:368px;width:313px;height:41px;border:2px solid var(--white);border-radius:14px;font-size:31px;display:flex;align-items:center;justify-content:center">FROM SCRATCH</div>
  <div class="cta cta--pink" style="left:168px;top:418px;width:135px;height:30px;font-size:11.5px">SIGN UP TODAY!</div>
</section>

<section class="card card--text">
  <div class="abs heavy" style="left:0;width:471px;text-align:center;top:30px;font-size:52px">THE LANTERN</div>
  <div class="abs condensed" style="left:0;width:471px;text-align:center;top:100px;font-size:44px">LEDGER PLAN</div>
  <svg style="position:absolute;left:0;top:0" width="471" height="471" viewBox="0 0 471 471" fill="none">
    <path d="M57 280V210H350M416 224V280" stroke="#f0345a" stroke-width="3"/>
  </svg>
  <div class="photo" role="img" aria-label="Illustration of a megaphone" style="left:352px;top:133px;width:90px;height:100px;border-radius:6px;background:linear-gradient(135deg,#e8f1f8 0%,#7badd7 100%)"></div>
  <div class="abs tag-white" style="left:140px;top:168px;font-size:24px;transform:rotate(-8deg)">HOW TO</div>
  <div class="abs tag-pink" style="left:165px;top:196px;font-size:24px;transform:rotate(-6deg)">LAUNCH A</div>
  <div class="abs headline" style="left:0;width:471px;text-align:center;top:228px;font-size:56px">MULTI-MILLION</div>
  <div class="abs" style="left:0;width:471px;text-align:center;top:290px;font-size:70px;font-weight:900;color:var(--pink)">BUSINESS</div>
  <div class="abs" style="left:0;width:471px;text-align:center;top:363px;font-size:27px;font-weight:700">FROM SCRATCH</div>
  <div class="cta cta--navy" style="left:167px;top:407px;width:136px;height:31px;font-size:11.5px">SIGN UP TODAY!</div>
</section>

<section class="card card--duo">
  <div class="photo" role="img" aria-label="Photo of the two course hosts, man with arms crossed and woman in a blue jacket" style="left:230px;top:93px;width:241px;height:378px;background:linear-gradient(90deg,#f0345a 0%,#1b1f2e 35%,#142a55 70%,#0d3c96 100%)"></div>
  <div class="abs heavy" style="left:17px;top:28px;font-size:54px">THE LANTERN</div>
  <div class="abs condensed" style="left:17px;top:96px;font-size:44px">LEDGER PLAN</div>
  <div class="abs tag-white" style="left:22px;top:172px;width:135px;font-size:26px;transform:rotate(-2deg);text-align:center">HOW TO</div>
  <div class="abs tag-pink" style="left:47px;top:205px;width:182px;font-size:24px;text-align:center">LAUNCH A</div>
  <div class="abs headline" style="left:22px;top:243px;font-size:61px">MULTI-MILLION</div>
  <div class="abs heavy" style="left:22px;top:308px;font-size:41px">BUSINESS</div>
  <div class="abs" style="left:22px;top:354px;font-size:33px;font-weight:400">FROM</div>
  <div class="abs heavy" style="left:20px;top:394px;font-size:38px">SCRATCH</div>
  <div class="cta cta--navy" style="left:297px;top:400px;width:150px;height:34px;font-size:12.5px">SIGN UP TODAY!</div>
</section>

</body>
</html>
```